Modern, upmarket label design for food product

We need a label design for a food company producing nuts with sesame and honey. In fact, we would like the words "Cashews med sesam & honning" on the label (It's in Danish and means - Cashews with sesame & honey). It should be easy for the customer to quickly understand what it is.

It is a shelf product in the competitive food industry, which is why the design should wake the feeling of 'just wanting to grab the product down from the shelves'. So, the design should stand out and have an image of a cool, modern, hip product. This being said, I love a raw & handmade look.

The company is called Tyvo. Its origins are from the danish word Pilt that is a Danish slang for yummy. I have uploaded a photo of the package the products will be sold in.

Info & dimensions on bag in picture 1.
Dimensions: 6" x 9" | 15.2 cm x 22.3 cm
Capacity: 8 ounces | 250 grams (based on whole bean coffee)

Picture 2 is the same product, but has the possibility of attaching to a hanger on shelfs.

Picture 3 - I have also uploaded a photo of a product bag, where the hole is linear instead of a round hole. The designer chooses, which bag they will like to work with!

Please let me know if there are any questions!

Target Market(s)

Target market could really be any age, but the design needs to compel the target audience to pick it from the shelves. The package should signal a product you want to hold and have other people seeing you have it. The target audience is people who cares for what they buy, and typically doesn't want a low-end or budget product. They want the whole thing, meaning it has to taste good, look good etc. They are also the type of people who like to show off whatever products they buy by placing them in their houses for their guests to see. Or by uploading pictures of it on social medias.

Industry/Entity Type

It Company

Font styles to use
Other font styles liked:
• Not a must, but I like the 'Panton' script

Requirements
Must have
• My project must have the words 'Cashews med sesam & honning' on the label, so the customer will know within a second what they are looking at and buying.
Nice to have
• I am picturing the label with the words 'Cashews med sesam & honning' as a statement, again, emphasizing how the customer instantly should know what the product is. This being said, it should not be the only thing on the package and I love a raw & handmade look - which inspiration picture 5 is a great example of!
• I have uploaded photos of what I think looks good. With this said, I am not looking for a copy of those products, but see them as good inspiration. I have named the photos inspiration 1, 2, 3, 4 & 5.
• If needed, more text can be put on the label. For example 'vegan', 'laktosefri', Glutenfri', or 'Sund Snack' are great words for being used on the label.
Should not have
• The fonts on the label should not be too decorative. Personally I like an easy too read font.

```html
<!DOCTYPE html>
<html lang="da">
<head>
<meta charset="utf-8">
<title>Tyvo – Cashews med sesam &amp; honning</title>
<link rel="stylesheet" href="https://fonts.googleapis.com/css2?family=Arvo:wght@700&family=Josefin+Slab:wght@300&family=Sniglet&display=swap">
<style>
  :root {
    --bg: #ffffff;
    --badge-brown: #47302a;
    --badge-shadow: #7a6a63;
    --chalk-white: #f4efe9;
    --honey-orange: #e29a17;
    --ribbon-fold: #a86f10;
  }
  html, body {
    margin: 0;
    padding: 0;
    width: 1200px;
    height: 695px;
    overflow: hidden;
    background: var(--bg);
  }
  .label-canvas {
    display: block;
    width: 1200px;
    height: 695px;
  }
  .badge-shadow { fill: var(--badge-shadow); }
  .badge-body { fill: var(--badge-brown); }
  .badge-inner-line {
    fill: none;
    stroke: var(--chalk-white);
    stroke-width: 3;
  }
  .brand-name {
    font-family: "Sniglet", sans-serif;
    font-size: 40px;
    fill: var(--honey-orange);
  }
  .brand-underline {
    fill: none;
    stroke: var(--honey-orange);
    stroke-width: 3;
    stroke-linecap: round;
  }
  .tagline {
    font-family: "Josefin Slab", serif;
    font-weight: 300;
    font-size: 70px;
    fill: none;
    stroke: var(--chalk-white);
    stroke-width: 1.6;
    letter-spacing: 2px;
  }
  .tagline-arc {
    fill: none;
    stroke: var(--chalk-white);
    stroke-width: 4;
    stroke-linecap: round;
  }
  .product-name {
    font-family: "Arvo", serif;
    font-weight: 700;
    font-size: 138px;
    fill: var(--chalk-white);
    letter-spacing: -2px;
  }
  .ribbon-band { fill: var(--honey-orange); }
  .ribbon-fold { fill: var(--ribbon-fold); }
  .ribbon-text {
    font-family: "Sniglet", sans-serif;
    font-size: 48px;
    fill: var(--chalk-white);
  }
  .ribbon-dot { fill: var(--chalk-white); }
</style>
</head>
<body>
<svg class="label-canvas" viewBox="0 0 1200 695" xmlns="http://www.w3.org/2000/svg" role="img" aria-label="Tyvo label: Sund Snack, Cashews med sesam og honning">
  <defs>
    <path id="scallop-outline" d="M910 347 A70 70 0 0 1 886.4 465.6 A70 70 0 0 1 819.2 566.2 A70 70 0 0 1 718.6 633.4 A70 70 0 0 1 600 657 A70 70 0 0 1 481.4 633.4 A70 70 0 0 1 380.8 566.2 A70 70 0 0 1 313.6 465.6 A70 70 0 0 1 290 347 A70 70 0 0 1 313.6 228.4 A70 70 0 0 1 380.8 127.8 A70 70 0 0 1 481.4 60.6 A70 70 0 0 1 600 37 A70 70 0 0 1 718.6 60.6 A70 70 0 0 1 819.2 127.8 A70 70 0 0 1 886.4 228.4 A70 70 0 0 1 910 347 Z"/>
    <path id="tagline-path" d="M370 300 Q600 140 830 300"/>
  </defs>

  <g class="badge">
    <use href="#scallop-outline" class="badge-shadow" transform="translate(6 8)"/>
    <use href="#scallop-outline" class="badge-body"/>
    <use href="#scallop-outline" class="badge-inner-line" transform="translate(600 347) scale(0.92) translate(-600 -347)" vector-effect="non-scaling-stroke"/>
  </g>

  <g class="brand">
    <text class="brand-name" x="600" y="128" text-anchor="middle">Tyvo</text>
    <path class="brand-underline" d="M560 142 Q600 150 642 138"/>
  </g>

  <text class="tagline"><textPath href="#tagline-path" startOffset="50%" text-anchor="middle">Sund Snack</textPath></text>
  <path class="tagline-arc" d="M445 330 Q600 230 755 330"/>

  <text class="product-name" x="600" y="425" text-anchor="middle">cashews</text>

  <g class="ribbon">
    <polygon class="ribbon-fold" points="300,458 340,450 340,520 310,540 325,500"/>
    <polygon class="ribbon-fold" points="900,458 860,450 860,520 890,540 875,500"/>
    <path class="ribbon-band" d="M318 458 Q600 430 882 458 L872 530 Q600 502 328 530 Z"/>
    <circle class="ribbon-dot" cx="350" cy="492" r="5"/>
    <circle class="ribbon-dot" cx="850" cy="492" r="5"/>
    <text class="ribbon-text" x="600" y="505" text-anchor="middle">med sesam &amp; honning</text>
  </g>
</svg>
</body>
</html>
```